Landing Page Design for Adult Dating Age Verification (18+)

The objective of this task is to design a visually appealing pre-landing page for the adult dating site "Plumvelle (site: https://plumvelle.example/)" with an age verification mechanism. The pre-landing page will feature two buttons that redirect visitors to the main offer. The design should also include a footer block that includes links to the terms of use, privacy policy, and contact us pages.

Design Requirements:
Develop an age verification section prominently displayed on the pre-landing page.
Design the section to include two buttons labeled "Yes" and "No" for visitors to confirm their age.
Ensure the section is visually appealing and clearly communicates the purpose of age verification.

Visual Appeal:
Create a visually appealing design that aligns with the branding and theme of the "Plumvelle" adult dating site.
Use suitable color schemes, typography, and graphics to enhance the overall visual appeal of the pre-landing page.

Layout and Navigation:
Design an engaging and intuitive layout that encourages visitors to interact with the page and proceed to the main offer.
Ensure clear and visible navigation elements that direct visitors to the main offer or provide additional information.

Responsive Design:
Develop a responsive design that provides a seamless user experience across various devices, including desktop and mobile.
Ensure the design elements and layout adapt well to different screen sizes and resolutions.

File Formats and Assets:
Deliver the final design in PSD, AI, or Sketch format, ensuring that the files are well-organized and layered.
Include any necessary images or assets used in the design, ensuring they are of high quality and optimized for web use.

```html
<!DOCTYPE html>
<html lang="en">
<head>
<meta charset="utf-8">
<title>Plumvelle — Age Verification</title>
<link rel="stylesheet" href="https://fonts.googleapis.com/css2?family=Montserrat:wght@400;500&family=Playfair+Display:wght@700;900&display=swap">
<style>
  :root {
    --ink: #000000;
    --lilac: #d5b6d7;
    --white: #ffffff;
    --alert-red: #ff2424;
    --footer-ink: #3b3340;
    --button-ink: #151515;
    --photo-warm: #4a3530;
    --photo-mid: #241a18;
  }
  * { margin: 0; padding: 0; box-sizing: border-box; }
  html, body {
    width: 1200px;
    height: 771px;
    overflow: hidden;
    background: var(--ink);
  }
  .page {
    position: relative;
    width: 1200px;
    height: 771px;
    background: var(--ink);
    color: var(--white);
    font-family: "Montserrat", Arial, sans-serif;
  }
  .hero-photo {
    position: absolute;
    left: 0;
    top: 27px;
    width: 1200px;
    height: 687px;
    background:
      radial-gradient(ellipse 45% 40% at 45% 55%, var(--photo-warm) 0%, transparent 100%),
      radial-gradient(ellipse 30% 35% at 20% 40%, #3b2a26 0%, transparent 100%),
      radial-gradient(ellipse 60% 25% at 60% 100%, #5a5552 0%, transparent 100%),
      linear-gradient(180deg, #0c0a0a 0%, var(--photo-mid) 55%, #2c2524 100%);
  }
  .brand {
    position: absolute;
    top: 52px;
    left: 0;
    width: 1200px;
    display: flex;
    justify-content: center;
    align-items: center;
    gap: 16px;
  }
  .brand-dot {
    width: 58px;
    height: 58px;
    border-radius: 50%;
    background: var(--lilac);
  }
  .brand-name {
    font-family: "Playfair Display", Georgia, serif;
    font-weight: 900;
    font-size: 44px;
    color: var(--white);
    line-height: 1;
  }
  .headline {
    position: absolute;
    top: 172px;
    left: 0;
    width: 1200px;
    text-align: center;
    font-family: "Playfair Display", Georgia, serif;
    font-weight: 900;
    font-size: 68px;
    line-height: 103px;
    letter-spacing: 1px;
  }
  .age-badge {
    display: inline-block;
    border: 2px solid var(--alert-red);
    border-radius: 2px;
    color: var(--alert-red);
    padding: 0 6px;
    line-height: 96px;
    margin-left: 14px;
    vertical-align: top;
    margin-top: 2px;
  }
  .age-badge .plus { font-weight: 400; font-family: "Montserrat", Arial, sans-serif; }
  .terms {
    position: absolute;
    top: 398px;
    left: 240px;
    width: 720px;
    text-align: center;
    font-size: 17px;
    line-height: 31px;
  }
  .terms p + p { margin-top: 30px; }
  .actions {
    position: absolute;
    top: 574px;
    left: 363px;
    display: flex;
    gap: 19px;
  }
  .btn {
    width: 228px;
    height: 68px;
    display: flex;
    align-items: center;
    justify-content: center;
    font-family: "Playfair Display", Georgia, serif;
    font-weight: 900;
    font-size: 29px;
    text-decoration: none;
    border: 2px solid var(--lilac);
    border-radius: 2px;
  }
  .btn-yes { background: var(--lilac); color: var(--button-ink); }
  .btn-no { background: transparent; color: var(--lilac); }
  .site-footer {
    position: absolute;
    left: 0;
    top: 714px;
    width: 1200px;
    height: 57px;
    background: var(--lilac);
    display: flex;
    align-items: center;
    justify-content: center;
    font-size: 17px;
    color: var(--footer-ink);
    letter-spacing: 0.3px;
  }
  .site-footer a { color: inherit; text-decoration: none; }
  .site-footer .divider { margin: 0 19px; }
</style>
</head>
<body>
<main class="page">
  <div class="hero-photo" role="img" aria-label="Dimmed photograph of a woman in black lingerie and stockings reclining on white fur"></div>

  <a class="brand" href="https://plumvelle.example/" aria-label="Plumvelle home">
    <span class="brand-dot"></span>
    <span class="brand-name">Plumvelle</span>
  </a>

  <h1 class="headline">
    ENTER ONLY IF YOU<br>
    ARE OVER <span class="age-badge">18<span class="plus">+</span></span>
  </h1>

  <div class="terms">
    <p>You are at least 18 (eighteen) years of age.</p>
    <p>You acknowledge you cannot, will not and shall not, use any material obtained by and through this site in any commercial or professional manner, for any reason, at any time.</p>
  </div>

  <nav class="actions">
    <a class="btn btn-yes" href="https://plumvelle.example/">YES</a>
    <a class="btn btn-no" href="https://plumvelle.example/">No</a>
  </nav>

  <footer class="site-footer">
    <a href="#">PRIVACY POLICY</a>
    <span class="divider">|</span>
    <a href="#">TERMS AND CONDITIONS</a>
    <span class="divider">|</span>
    <a href="#">CANCEL SUBSCRIPTION</a>
  </footer>
</main>
</body>
</html>
```